Flyer overhaul from current flyers

I need to have our current flyers updated with a fresher look. We also need to have a new utility and real estate flyer created that will go along with the design of the new flyer. We are looking for new pictures, new overall design, same color scheme but would like to have the flyers more airy and inviting.

Target Market(s)

decision makers in the healthcare/utilty/banking/real estate sectors

Font styles to use
Other font styles liked:
• Logo is in Bell MT

Colors
0054AA
0677BA
7BADD7
CADEEF
E8F1F8

Requirements
Must have
• Close to what is currently on the existing flyers

```html
<!DOCTYPE html>
<html lang="en">
<head>
<meta charset="utf-8">
<title>Riverbend Settlement – Flyers</title>
<link href="https://fonts.googleapis.com/css2?family=Montserrat:ital,wght@0,400;0,500;0,600;0,700;0,800;1,500&display=swap" rel="stylesheet">
<style>
:root{
  --navy:#0054AA;
  --blue:#0677BA;
  --sky:#7BADD7;
  --mist:#CADEEF;
  --ice:#E8F1F8;
  --bright:#0A93D3;
  --charcoal:#2F3133;
  --ink:#333538;
  --stage:#E4E5E6;
  --white:#FFFFFF;
}
*{margin:0;padding:0;box-sizing:border-box}
html,body{width:1200px;height:3515px;overflow:hidden}
body{background:var(--stage);font-family:'Montserrat',sans-serif;position:relative}
.flyer{position:absolute;left:50px;width:1100px;height:1425px;background:var(--white);overflow:hidden;box-shadow:0 6px 24px rgba(0,0,0,.12)}
.flyer--services{top:180px}
.flyer--philosophy{top:1855px}
.flyer svg.shapes{position:absolute;inset:0;width:1100px;height:1425px}
.brand{position:absolute;left:60px;top:66px;display:flex;align-items:center;gap:20px;color:var(--white)}
.brand__dot{width:90px;height:90px;border-radius:50%;background:var(--blue)}
.brand__name{font-weight:600;font-size:38px;line-height:1.05;letter-spacing:1px}
.hero-title{position:absolute;left:77px;top:600px;color:var(--white);font-weight:800;font-size:70px;line-height:1.05;letter-spacing:.5px}
.band-title{position:absolute;left:77px;top:808px;color:var(--white);font-weight:800;font-size:31px;line-height:1.03}
.features{position:absolute;left:82px;top:920px;list-style:none}
.features li{position:relative;height:0}
.feature{position:absolute;left:0;display:flex;align-items:center;gap:30px;width:560px;color:var(--ink);font-weight:600;font-size:25px;line-height:1.25;transform:translateY(-50%)}
.feature svg{flex:none;width:44px;height:44px}
.solution-title{position:absolute;left:675px;top:786px;color:var(--white);font-weight:800;font-size:30px;line-height:1.1}
.solutions{position:absolute;left:680px;top:868px;list-style:none;color:var(--white);font-size:23px;line-height:34px;font-weight:500}
.solutions li{display:flex;gap:12px;align-items:flex-start}
.solutions li svg{flex:none;width:18px;height:18px;margin-top:8px}
.footer-line{position:absolute;left:66px;display:flex;align-items:center;gap:12px;color:var(--white);font-size:29px;font-weight:500;letter-spacing:2px}
.footer-line svg{width:24px;height:24px}
.footer-line--services{top:1361px}
.footer-line--philosophy{top:1352px}
.philosophy-title{position:absolute;left:0;width:1100px;top:858px;text-align:center;color:var(--blue);font-weight:800;font-size:62px;letter-spacing:.5px}
.philosophy-copy{position:absolute;left:125px;width:850px;top:950px;text-align:center;color:var(--ink);font-size:19.5px;line-height:25px}
.philosophy-copy p+p{margin-top:20px}
.contact-title{position:absolute;left:70px;top:1231px;color:var(--white);font-weight:700;font-size:33px;letter-spacing:1px}
.contact-line{position:absolute;left:62px;top:1292px;color:var(--bright);font-style:italic;font-weight:500;font-size:31px}
</style>
</head>
<body>

<section class="flyer flyer--services">
  <svg class="shapes" viewBox="0 0 1100 1425" aria-hidden="true">
    <defs>
      <linearGradient id="panelGrad" x1="0" y1="0" x2="1" y2="1">
        <stop offset="0" stop-color="#0677BA"/>
        <stop offset="1" stop-color="#0054AA"/>
      </linearGradient>
      <linearGradient id="heroGrad" x1="0" y1="0" x2="1" y2="1">
        <stop offset="0" stop-color="#0b2e5e"/>
        <stop offset=".45" stop-color="#1d6fb8"/>
        <stop offset=".75" stop-color="#0c4a8a"/>
        <stop offset="1" stop-color="#07284f"/>
      </linearGradient>
      <linearGradient id="bandGrad" x1="0" y1="0" x2="1" y2="0">
        <stop offset="0" stop-color="#0A93D3"/>
        <stop offset="1" stop-color="#0677BA"/>
      </linearGradient>
    </defs>
    <rect x="0" y="77" width="1100" height="696" fill="url(#heroGrad)" role="img" aria-label="Photo of a hand using a digital banking interface with glowing bank icon"/>
    <polygon points="0,0 1100,0 1100,77 640,77 580,222 0,222" fill="var(--charcoal)"/>
    <rect x="640" y="77" width="460" height="10" fill="var(--blue)"/>
    <polygon points="0,802 572,802 540,885 0,885" fill="url(#bandGrad)"/>
    <polygon points="660,725 1100,725 1100,1334 624,1334 624,770" fill="url(#panelGrad)"/>
    <rect x="0" y="1334" width="1100" height="91" fill="var(--charcoal)"/>
  </svg>

  <div class="brand">
    <div class="brand__dot"></div>
    <div class="brand__name">RIVERBEND<br>SETTLEMENT</div>
  </div>

  <h1 class="hero-title">FINANCIAL<br>COLLECTIONS</h1>
  <h2 class="band-title">A FORWARD<br>THINKING APPROACH</h2>

  <ul class="features">
    <li><div class="feature" style="top:27px"><svg viewBox="0 0 44 44" fill="none" stroke="#0054AA" stroke-width="2.2"><circle cx="22" cy="22" r="19"/><circle cx="22" cy="17" r="6"/><path d="M11 33c2-6 6-8 11-8s9 2 11 8"/></svg>Consumer Friendly,<br>Professional Approach</div></li>
    <li><div class="feature" style="top:108px"><svg viewBox="0 0 44 44" fill="none" stroke="#0054AA" stroke-width="2.2"><rect x="6" y="8" width="32" height="22" rx="3"/><path d="M16 38h12M22 30v8"/><circle cx="22" cy="19" r="5"/></svg>Online Consumer Debt<br>Negotiation Tools</div></li>
    <li><div class="feature" style="top:182px"><svg viewBox="0 0 44 44" fill="none" stroke="#0054AA" stroke-width="2.2"><path d="M8 24v-3a14 14 0 0 1 28 0v3"/><rect x="5" y="23" width="7" height="11" rx="2"/><rect x="32" y="23" width="7" height="11" rx="2"/><path d="M35 34c0 4-5 6-10 6"/></svg>Live Online Agent Chat Portals</div></li>
    <li><div class="feature" style="top:253px"><svg viewBox="0 0 44 44" fill="none" stroke="#0054AA" stroke-width="2.2"><rect x="8" y="5" width="24" height="34" rx="2"/><path d="M13 13h14M13 19h14M13 25h8"/><path d="M26 33l10-12 3 3-10 12-4 1z"/></svg>Online Consumer Dispute/<br>Complaint Tools</div></li>
    <li><div class="feature" style="top:333px"><svg viewBox="0 0 44 44" fill="none" stroke="#0054AA" stroke-width="2.2"><path d="M22 4l15 6v10c0 10-7 17-15 20C14 37 7 30 7 20V10z"/><circle cx="22" cy="20" r="3"/><path d="M22 23v6"/></svg>FISMA Compliant Physical<br>and Virtual Security</div></li>
  </ul>

  <h2 class="solution-title">AN IMPACTFUL,<br>ALL-IN-ONE SOLUTION</h2>
  <ul class="solutions">
    <li><svg viewBox="0 0 18 18"><circle cx="9" cy="9" r="9" fill="#fff"/><path d="M5 9.3l2.6 2.6L13 6.5" fill="none" stroke="#0677BA" stroke-width="2.2"/></svg>Credit Report Monitoring</li>
    <li><svg viewBox="0 0 18 18"><circle cx="9" cy="9" r="9" fill="#fff"/><path d="M5 9.3l2.6 2.6L13 6.5" fill="none" stroke="#0677BA" stroke-width="2.2"/></svg>Address/Phone Scrubbing</li>
    <li><svg viewBox="0 0 18 18"><circle cx="9" cy="9" r="9" fill="#fff"/><path d="M5 9.3l2.6 2.6L13 6.5" fill="none" stroke="#0677BA" stroke-width="2.2"/></svg>Compliant Collection Letters</li>
    <li><svg viewBox="0 0 18 18"><circle cx="9" cy="9" r="9" fill="#fff"/><path d="M5 9.3l2.6 2.6L13 6.5" fill="none" stroke="#0677BA" stroke-width="2.2"/></svg>Discretionary Credit Reporting</li>
    <li><svg viewBox="0 0 18 18"><circle cx="9" cy="9" r="9" fill="#fff"/><path d="M5 9.3l2.6 2.6L13 6.5" fill="none" stroke="#0677BA" stroke-width="2.2"/></svg><span>Customizable Collection<br>Workflow</span></li>
    <li><svg viewBox="0 0 18 18"><circle cx="9" cy="9" r="9" fill="#fff"/><path d="M5 9.3l2.6 2.6L13 6.5" fill="none" stroke="#0677BA" stroke-width="2.2"/></svg>Professional Skip Tracing</li>
    <li><svg viewBox="0 0 18 18"><circle cx="9" cy="9" r="9" fill="#fff"/><path d="M5 9.3l2.6 2.6L13 6.5" fill="none" stroke="#0677BA" stroke-width="2.2"/></svg>Deceased/Probate Services</li>
    <li><svg viewBox="0 0 18 18"><circle cx="9" cy="9" r="9" fill="#fff"/><path d="M5 9.3l2.6 2.6L13 6.5" fill="none" stroke="#0677BA" stroke-width="2.2"/></svg>Call Recording and Monitoring</li>
    <li><svg viewBox="0 0 18 18"><circle cx="9" cy="9" r="9" fill="#fff"/><path d="M5 9.3l2.6 2.6L13 6.5" fill="none" stroke="#0677BA" stroke-width="2.2"/></svg>Bankruptcy Claim Services</li>
    <li><svg viewBox="0 0 18 18"><circle cx="9" cy="9" r="9" fill="#fff"/><path d="M5 9.3l2.6 2.6L13 6.5" fill="none" stroke="#0677BA" stroke-width="2.2"/></svg>Legal Collection Services</li>
    <li><svg viewBox="0 0 18 18"><circle cx="9" cy="9" r="9" fill="#fff"/><path d="M5 9.3l2.6 2.6L13 6.5" fill="none" stroke="#0677BA" stroke-width="2.2"/></svg>Utility Collection</li>
    <li><svg viewBox="0 0 18 18"><circle cx="9" cy="9" r="9" fill="#fff"/><path d="M5 9.3l2.6 2.6L13 6.5" fill="none" stroke="#0677BA" stroke-width="2.2"/></svg>Property Management</li>
  </ul>

  <div class="footer-line footer-line--services">
    <svg viewBox="0 0 24 24"><circle cx="12" cy="12" r="12" fill="#0A93D3"/><path d="M8 6.5l2.2 2.4-1.2 1.6c.8 1.8 2 3 3.8 3.8l1.6-1.2 2.4 2.2-1.3 1.9c-4.6-.4-8.4-4.2-8.8-8.8z" fill="#2F3133"/></svg>
    <span>(555) 014-2870 |</span>
    <svg viewBox="0 0 24 24" fill="none" stroke="#0A93D3" stroke-width="1.8"><circle cx="12" cy="12" r="10"/><ellipse cx="12" cy="12" rx="4.5" ry="10"/><path d="M2 12h20"/></svg>
    <span>WWW.RIVERBENDSETTLEMENT.COM</span>
  </div>
</section>

<section class="flyer flyer--philosophy">
  <svg class="shapes" viewBox="0 0 1100 1425" aria-hidden="true">
    <defs>
      <linearGradient id="tabletGrad" x1="0" y1="0" x2="0" y2="1">
        <stop offset="0" stop-color="#dfe3e8"/>
        <stop offset=".55" stop-color="#EEF3F8"/>
        <stop offset="1" stop-color="#ffffff"/>
      </linearGradient>
    </defs>
    <rect x="0" y="77" width="1100" height="780" fill="url(#tabletGrad)" role="img" aria-label="Photo of a white tablet showing an online banking word cloud in blue"/>
    <polygon points="0,0 1100,0 1100,77 640,77 580,222 0,222" fill="var(--charcoal)"/>
    <polygon points="0,1210 320,1210 336,1231 1100,1231 1100,1425 0,1425" fill="var(--charcoal)"/>
    <polygon points="336,1231 1100,1231 1100,1256 352,1256" fill="var(--blue)"/>
  </svg>

  <div class="brand">
    <div class="brand__dot"></div>
    <div class="brand__name">RIVERBEND<br>SETTLEMENT</div>
  </div>

  <h1 class="philosophy-title">OUR PHILOSOPHY</h1>
  <div class="philosophy-copy">
    <p>For over 40 years, Riverbend Settlement has assisted banks and financial services companies in the reconciliation of their past due accounts. Our philosophy is to provide consistent performance by investing in our clients’ accounts to ensure the maximum liquidation. By building on historically proven collection techniques and employing an ever-expanding access to data and technology, our agency has continued to improve our performance to the benefit of our clients.</p>
    <p>Our capital forward, compliance centered approach has proven to deliver the most consistent results for our financial service providers.</p>
  </div>

  <h2 class="contact-title">CONTACT US</h2>
  <p class="contact-line">To Discuss Which Of Our Services Can Best Serve Your Business.</p>

  <div class="footer-line footer-line--philosophy">
    <svg viewBox="0 0 24 24"><circle cx="12" cy="12" r="12" fill="#0A93D3"/><path d="M8 6.5l2.2 2.4-1.2 1.6c.8 1.8 2 3 3.8 3.8l1.6-1.2 2.4 2.2-1.3 1.9c-4.6-.4-8.4-4.2-8.8-8.8z" fill="#2F3133"/></svg>
    <span>(555) 014-2870 |</span>
    <svg viewBox="0 0 24 24" fill="none" stroke="#0A93D3" stroke-width="1.8"><circle cx="12" cy="12" r="10"/><ellipse cx="12" cy="12" rx="4.5" ry="10"/><path d="M2 12h20"/></svg>
    <span>WWW.RIVERBENDSETTLEMENT.COM</span>
  </div>
</section>

</body>
</html>
```